Driving School
Brightlane Driving School
Project: Driving School
Driving School - Automotive
Creative Brief
Professional
214-52 Hollister Avenue Jamaica NY 11432
brightlanedriving@mailnest.example
www.BrightlaneDriving.example
Car & CDL Training
Calendar Or Driving school Directional MAP

```html
<!DOCTYPE html>
<html lang="en">
<head>
<meta charset="utf-8">
<title>Brightlane Driving School – Business Cards</title>
<link href="https://fonts.googleapis.com/css2?family=Montserrat:wght@500;600;800&display=swap" rel="stylesheet">
<style>
  :root {
    --backdrop: #e9eaec;
    --brand-blue: #1f5fa8;
    --brand-blue-light: #3a86cf;
    --brand-blue-dark: #184c8a;
    --brand-red: #d7262e;
    --ink: #3a4654;
    --paper: #ffffff;
  }
  * { box-sizing: border-box; margin: 0; padding: 0; }
  html, body { width: 1200px; height: 864px; overflow: hidden; }
  body {
    background: var(--backdrop);
    font-family: "Montserrat", sans-serif;
    position: relative;
  }
  .card {
    position: absolute;
    width: 520px;
    height: 297px;
    border-radius: 18px;
    overflow: hidden;
    box-shadow: 0 12px 30px rgba(0,0,0,.18);
  }
  /* Front */
  .card-front {
    left: 60px; top: 230px;
    background: radial-gradient(ellipse at 45% 40%, var(--brand-blue-light) 0%, var(--brand-blue) 55%, var(--brand-blue-dark) 100%);
    color: var(--paper);
  }
  .card-front .brand-name {
    position: absolute;
    left: 0; right: 0; top: 112px;
    text-align: center;
    font-weight: 800;
    font-size: 38px;
    letter-spacing: 1px;
    text-transform: uppercase;
  }
  .card-front .website {
    position: absolute;
    left: 0; right: 0; bottom: 26px;
    text-align: center;
    font-weight: 500;
    font-size: 11px;
    letter-spacing: 3px;
    text-transform: uppercase;
  }
  /* Back */
  .card-back {
    left: 620px; top: 340px;
    background: var(--paper);
  }
  .card-back .swoosh { position: absolute; inset: 0; }
  .card-back .brand-block {
    position: absolute;
    left: 28px; top: 58px;
    width: 230px;
  }
  .card-back .brand-name {
    font-weight: 800;
    font-size: 26px;
    line-height: 1.05;
    color: var(--brand-blue);
    text-transform: uppercase;
  }
  .card-back .holder {
    margin-top: 26px;
    font-weight: 600;
    font-size: 12px;
    letter-spacing: 2px;
    color: var(--brand-blue);
    text-transform: uppercase;
  }
  .card-back .address {
    margin-top: 6px;
    font-weight: 500;
    font-size: 9px;
    letter-spacing: 1px;
    line-height: 1.5;
    color: var(--ink);
    text-transform: uppercase;
  }
  .contact-list {
    position: absolute;
    left: 284px; top: 66px;
    list-style: none;
  }
  .contact-list li {
    display: flex;
    align-items: center;
    gap: 8px;
    height: 22px;
    font-weight: 500;
    font-size: 10px;
    color: var(--ink);
  }
  .contact-list .icon {
    width: 15px; height: 15px;
    flex: none;
  }
</style>
</head>
<body>

<section class="card card-front" aria-label="Business card front">
  <div class="brand-name">Brightlane</div>
  <div class="website">www.BrightlaneDriving.example</div>
</section>

<section class="card card-back" aria-label="Business card back">
  <svg class="swoosh" viewBox="0 0 520 297" preserveAspectRatio="none" aria-hidden="true">
    <path d="M0 297 Q280 268 520 168 L520 206 Q330 282 140 297 Z" fill="var(--brand-red)"/>
    <path d="M190 297 Q390 272 520 218 L520 297 Z" fill="var(--brand-blue)"/>
    <path d="M0 262 Q60 290 150 297 L0 297 Z" fill="var(--brand-blue)"/>
  </svg>

  <div class="brand-block">
    <div class="brand-name">Brightlane<br>Driving School</div>
    <div class="holder">Daniel Reyes</div>
    <div class="address">214-52 Hollister Avenue<br>Jamaica NY 11432</div>
  </div>

  <ul class="contact-list">
    <li>
      <svg class="icon" viewBox="0 0 16 16" aria-hidden="true"><circle cx="8" cy="8" r="8" fill="var(--brand-blue)"/><path d="M5.5 4h1.6l.7 2-1 .8a6 6 0 0 0 2.4 2.4l.8-1 2 .7v1.6c0 .4-.4.8-.8.8A7.2 7.2 0 0 1 4.7 4.8c0-.4.4-.8.8-.8z" fill="#fff"/></svg>
      718-555-0142
    </li>
    <li>
      <svg class="icon" viewBox="0 0 16 16" aria-hidden="true"><circle cx="8" cy="8" r="8" fill="var(--brand-red)"/><path d="M5.5 4h1.6l.7 2-1 .8a6 6 0 0 0 2.4 2.4l.8-1 2 .7v1.6c0 .4-.4.8-.8.8A7.2 7.2 0 0 1 4.7 4.8c0-.4.4-.8.8-.8z" fill="#fff"/></svg>
      718-555-0187
    </li>
    <li>
      <svg class="icon" viewBox="0 0 16 16" aria-hidden="true"><circle cx="8" cy="8" r="8" fill="var(--brand-blue)"/><rect x="4" y="5" width="8" height="6" rx="1" fill="#fff"/><path d="M4.3 5.4 8 8.3l3.7-2.9" stroke="var(--brand-blue)" stroke-width=".9" fill="none"/></svg>
      brightlanedriving@mailnest.example
    </li>
    <li>
      <svg class="icon" viewBox="0 0 16 16" aria-hidden="true"><circle cx="8" cy="8" r="8" fill="var(--brand-blue)"/><circle cx="8" cy="8" r="4" stroke="#fff" stroke-width="1" fill="none"/><path d="M4 8h8M8 4c-2 2.4-2 5.6 0 8M8 4c2 2.4 2 5.6 0 8" stroke="#fff" stroke-width=".8" fill="none"/></svg>
      www.BrightlaneDriving.example
    </li>
  </ul>
</section>

</body>
</html>
```